Geschäftspapiere für Fliesenleger - Meisterbetrieb
Zielgruppe
Wir sind ein mittelständischer Fliesenleger - Meisterbetrieb und möchten unsere Geschäftspapiere erneuern. Unsere Kunden sind Privatkunden, Gewerbetreibende sowie Öffentliche Auftraggeber.
Aufgabenstellung
Unser Logo stellen wir Ihnen zur verfügung und soll unverändert bleiben.
Wir benötigen folgende Geschäftspapiere:
- Briefpapier DIN A4
- Notizblock Karriert DIN A4
- Visitenkarten 5,5 x 8,5 cm
- Kuvert DIN lang mit Fenster
- Kuvert DIN C4 mit Fenster
Bei der Farbe Rot handelt es sich um Verkehrsrot RAL 3020
Als Schriftart haben wir uns Helvetica Neue vorgestellt.
Wir bitten jedoch auch um Vorschläge anderer Moderner und gut lesbarer Schriftarten die für Print und Web bestens geeignet sind.
Wir wünschen uns ein Modernes und Schnörkelloses Design. Bei den Dateien habe ich Ihnen ein Stockphoto angehängt um Ihnen zu zeigen wie wir uns ein Cover oder eine Broschüre vorstellen können. Nur um Ihnen unsere Ideen / Vorstellungen näher zu bringen.

```html
<!DOCTYPE html>
<html lang="de">
<head>
<meta charset="utf-8">
<title>Fliesen-Kerner Geschäftspapiere</title>
<link rel="stylesheet" href="https://fonts.googleapis.com/css2?family=Inter:wght@400;700&display=swap">
<style>
:root{
  --paper:#ffffff;
  --stage:#ffffff;
  --ink:#1d1d1b;
  --red:#c1121c;
  --blush:#f0c9cb;
  --rule:#3a3a3a;
  --shadow:0 4px 14px rgba(0,0,0,.16);
}
*{margin:0;padding:0;box-sizing:border-box}
html,body{width:1071px;height:1200px;overflow:hidden;background:var(--stage)}
body{position:relative;font-family:"Inter",Arial,sans-serif;color:var(--ink)}
.sheet{position:absolute;background:var(--paper);box-shadow:var(--shadow)}
.letterhead{left:64px;top:139px;width:660px;height:933px}
.brand-name{position:absolute;font-weight:700;color:var(--red);letter-spacing:-.2px;white-space:nowrap}
.letterhead .brand-name{right:54px;top:72px;font-size:23px}
.sender-line{position:absolute;left:54px;top:90px;font-size:7.6px;word-spacing:1px}
.sender-line span{margin-right:10px}
.recipient{position:absolute;left:54px;top:160px;font-size:9.5px;line-height:12px}
.side-block{position:absolute;left:437px;border-left:1px solid var(--rule);padding-left:7px;font-size:9.5px;line-height:12px}
.side-block.contact{top:160px}
.side-block.bank{top:789px}
.gap{height:12px}
.meta{position:absolute;top:287px;left:55px;right:51px;display:flex;justify-content:space-between;font-weight:700;font-size:9.5px}
.salutation{position:absolute;left:55px;top:371px;font-size:9.5px}
.body-text{position:absolute;left:55px;top:419px;width:555px;font-size:9.5px;line-height:12px}
.closing{position:absolute;left:55px;top:538px;font-size:9.5px}
.tagline-area{position:absolute;left:46px;top:780px;width:312px;height:101px;background:linear-gradient(100deg,rgba(240,201,203,.55),rgba(240,201,203,.25));border-radius:6px}
.card{width:267px;height:174px}
.card.front{left:752px;top:502px}
.card.back{left:752px;top:725px}
.card.front .brand-name{left:0;right:0;text-align:center;top:86px;font-size:21px}
.card.back .brand-name{right:17px;top:31px;font-size:14px}
.card-contact{position:absolute;left:17px;top:73px;font-size:7.7px;line-height:10px}
.card-contact .gap{height:10px}
.card-person{position:absolute;right:16px;top:128px;text-align:right}
.card-person .name{font-weight:700;font-size:11.5px}
.card-person .role{font-size:7.7px}
</style>
</head>
<body>
<section class="sheet letterhead">
  <div class="sender-line"><span>KRNR Kerner GmbH</span><span>Lindenweg 14</span><span>91099 Talheim</span></div>
  <div class="brand-name">Fliesen-Kerner</div>
  <address class="recipient" style="font-style:normal">Frau Susanne Muster<br>Dorfstraße 121<br>91099 Talheim</address>
  <div class="side-block contact">
    KRNR Kerner GmbH<br>Lindenweg 14<br>91099 Talheim
    <div class="gap"></div>
    Tel.: 09123-4560100<br>Fax: 09123-4560177<br>Email: post@fliesen-kerner.de<br>Web: www.fliesen-kerner.de
  </div>
  <div class="meta"><span>Rechnungsnr.:</span><span>Talheim, 06.Mai 2025</span></div>
  <p class="salutation">Sehr geehrte Frau Muster,</p>
  <p class="body-text">Lorem ipsum dolor sit amet, consectetuer adipiscing elit, sed diam nonummy nibh euismod tincidunt ut laoreet dolore magna aliquam erat volutpat. Ut wisi enim ad minim veniam, quis nostrud exerci tation ullamcorper suscipit lobortis nisl ut aliquip ex ea commodo consequat. Duis autem vel eum iriure dolor in hendrerit in vulputate velit esse molestie consequat, vel illum dolore eu feugiat nulla facilisis at vero eros et accumsan et iusto odio dignissim qui blandit praesent luptatum zzril delenit augue duis dolore te feugait nulla facilisi.<br>Lorem ipsum dolor sit amet, cons ectetuer adipiscing elit, sed diam nonummy nibh euismod tincidunt ut laoreet dolore magna aliquam erat volutpat. Ut wisi enim ad minim veniam, quis nostrud exerci tation ullamcorper suscipit lobortis nisl ut aliquip ex ea commodo consequat.</p>
  <p class="closing">Mit freundlichen Grüßen</p>
  <div class="tagline-area" role="img" aria-label="Faint hand-lettered slogan decoration"></div>
  <div class="side-block bank">
    Bankverbindung:<br>Raiffeisenbank Talgrund<br>IBAN: DE00 0000 0000 0000 0000 00<br>BIC: GENODEF1TLG
    <div class="gap"></div>
    Geschäftsführer: Malte Kerner<br>HRB 4521 Amtsgericht Talheim<br>Ust. ID: DE204517986
  </div>
</section>

<section class="sheet card front">
  <div class="brand-name">Fliesen-Kerner</div>
</section>

<section class="sheet card back">
  <div class="brand-name">Fliesen-Kerner</div>
  <div class="card-contact">
    KRNR Kerner GmbH<br>Lindenweg 14<br>91099 Talheim
    <div class="gap"></div>
    Tel.: 09123-4560100<br>Fax: 09123-4560177<br>Email: post@fliesen-kerner.de<br>Web: www.fliesen-kerner.de
  </div>
  <div class="card-person"><div class="name">Malte Kerner</div><div class="role">Geschäftsführer</div></div>
</section>
</body>
</html>
```